Sports Nutrition Supplement Label design

We need a sports supplement label design for an existing business. (I have provided our business logo in the file uploads) These labels will remain consistent across the product line with the name of the product being the only changing field. The current product names (example: "vegan") on the labels provided are just for reference, the ingredients portions etc are final, but the actual name will be changed to something less generic for each product. I will just need to be able to change the name and have it match with label concept. We would like the look to be professional, clean, and exemplify quality. Please reference our business website kelvardathletic.com to get a feel for design and brand association.
I have also included the QVR supplement label guidelines so we are certain to maintain compliance.
Thank you and I'm looking forward to working with you and seeing your creative designs!
Doug
Updates

Target Market(s)

Athletes, Sports professionals, Colleges, Professional Sports Teams

Industry/Entity Type

Sports Science/ Sports Training/Athletics

Requirements
Nice to have
• I would like the design to possibly reflect these key terms: Sport Science, Chemistry, Clean, Professional, Quality (We also like water/ocean/waves concepts but is not a "requirement" it would have to really work well in the design somehow to appeal to wide range of athletes)

```html
<!DOCTYPE html>
<html lang="en">
<head>
<meta charset="UTF-8">
<title>Kelvard Athletic BCAA Label</title>
<link rel="stylesheet" href="https://fonts.googleapis.com/css2?family=Barlow:wght@500;600&family=Barlow+Condensed:wght@500;600&family=Barlow+Semi+Condensed:wght@700&family=Jost:wght@400&display=swap">
<style>
  :root {
    --backdrop: #e4e4e4;
    --label-white: #f7f7f7;
    --label-shade: #ececec;
    --ink: #1c1c1c;
    --ink-soft: #3d3d3d;
    --green-bright: #2ed12a;
    --green-light: #93ea8d;
    --green-deep: #1a7a1f;
    --green-tab: #39d430;
    --text-on-green: #ffffff;
    --text-band: #173317;
  }
  * { margin: 0; padding: 0; box-sizing: border-box; }
  html, body { width: 1200px; height: 900px; overflow: hidden; }
  body { background: var(--backdrop); position: relative; }

  .label {
    position: absolute; left: 240px; top: 50px;
    width: 720px; height: 800px;
    background: linear-gradient(90deg, var(--label-shade) 0%, var(--label-white) 30%, var(--label-white) 75%, var(--label-shade) 100%);
    overflow: hidden;
  }

  .brand { position: absolute; left: 68px; top: 66px; color: var(--ink-soft); font-family: "Jost", sans-serif; font-weight: 400; }
  .brand-name { font-size: 84px; line-height: 1; letter-spacing: 6px; }
  .brand-sub { font-size: 25px; letter-spacing: 9px; margin-top: 18px; }

  .product-name {
    position: absolute; left: 62px; top: 222px;
    font-family: "Barlow Semi Condensed", sans-serif; font-weight: 700;
    font-size: 252px; line-height: 1; letter-spacing: -2px; color: var(--ink);
  }
  .product-desc {
    position: absolute; left: 68px; top: 478px;
    font-family: "Barlow", sans-serif; font-weight: 500; font-size: 27px; color: var(--ink-soft);
  }

  .flavor-tab {
    position: absolute; left: 442px; top: 530px; width: 278px; height: 48px;
    background: var(--green-tab); border-top-left-radius: 22px;
    color: var(--text-on-green); font-family: "Barlow", sans-serif; font-weight: 600;
    font-size: 28px; line-height: 48px; padding-left: 50px; letter-spacing: 0.5px;
  }

  .green-band {
    position: absolute; left: 0; top: 575px; width: 720px; height: 225px;
    background: linear-gradient(90deg, var(--green-light) 0%, var(--green-bright) 45%, var(--green-bright) 75%, #7ad874 100%);
  }
  .claims-panel {
    position: absolute; left: 0; top: 0; width: 571px; height: 140px;
    background: var(--green-deep); border-bottom-right-radius: 42px;
    display: flex; align-items: flex-start; padding: 34px 0 0 68px;
    font-family: "Barlow Condensed", sans-serif; color: var(--text-on-green);
  }
  .claim { padding: 0 20px; border-left: 2px solid rgba(255,255,255,0.55); }
  .claim:first-child { padding-left: 0; border-left: none; }
  .claim-title { font-size: 52px; font-weight: 600; line-height: 0.95; }
  .claim-note { font-size: 20px; font-weight: 500; margin-top: 4px; }

  .band-footer {
    position: absolute; left: 70px; top: 162px;
    font-family: "Barlow Condensed", sans-serif; font-weight: 500; font-size: 26px;
    color: var(--text-band); letter-spacing: 0.2px;
  }
  .band-footer .divider { margin: 0 10px; }

  .net-weight {
    position: absolute; right: 18px; top: 115px; text-align: right;
    font-family: "Barlow Condensed", sans-serif; font-weight: 500; font-size: 22px;
    line-height: 1.7; color: #2d4f2d;
  }
</style>
</head>
<body>
  <section class="label">
    <div class="brand">
      <div class="brand-name">KELVARD</div>
      <div class="brand-sub">ATHLETIC</div>
    </div>

    <h1 class="product-name">BCAA</h1>
    <p class="product-desc">Branched Chain Amino Acids</p>

    <div class="flavor-tab">LEMON LIME</div>

    <div class="green-band">
      <div class="claims-panel">
        <div class="claim">
          <div class="claim-title">BCAA</div>
          <div class="claim-note">Ratio 2:1:1</div>
        </div>
        <div class="claim">
          <div class="claim-title">SUPPORTS</div>
          <div class="claim-note">Muscle Building</div>
        </div>
        <div class="claim">
          <div class="claim-title">SPEEDS</div>
          <div class="claim-note">Recovery</div>
        </div>
      </div>
      <div class="net-weight">NET WT. 325 G<br>(11.46 OZ)</div>
      <p class="band-footer">NATURAL &amp; ARTIFICIAL FLAVOR<span class="divider">|</span>DIETARY SUPPLEMENT</p>
    </div>
  </section>
</body>
</html>
```